Radiant Harbor Chocolate Shake Label

We need a new label design for our Radiant Harbor Chocolate Protein Shake. The design needs to include all the composition info as per the attached Lumo Grace Chocolate shake label with a fresh new eye catching design that will stand out on retail store shelves. It must include our Radiant Harbor Logo and portray a professional image that inspires trust. It must indicate that it is a chocolate shake that looks tasty and inviting. Radiant Harbor is a product sold by healthcare practitioners.

Industry/Entity Type

Health And Wellness

Requirements
Must have
• The Radiant Harbor logo. Contain all the attached info as per the chocolate Lumo Grace label. Feature something that indicates it is a chocolate shake on the label that looks tasty and inviting.
Nice to have
• I have attached some of the other products in our range. Would be a bonus if it can match into the existing look and feel somehow.

```html
<!DOCTYPE html>
<html lang="en">
<head>
<meta charset="UTF-8">
<title>Radiant Harbor Chocolate Protein Shake Label</title>
<link rel="stylesheet" href="https://fonts.googleapis.com/css2?family=Oswald:wght@500;700&display=swap">
<style>
  :root {
    --backdrop: #b07d4f;
    --label-white: #f4f4f2;
    --cocoa-dark: #4a2c1d;
    --cocoa-mid: #7a4f37;
    --cocoa-light: #a77a58;
    --text-light: #ffffff;
    --text-dark: #3b2418;
    --logo-blue: #2d4f8c;
  }
  * { margin: 0; padding: 0; box-sizing: border-box; }
  html, body {
    width: 1200px;
    height: 961px;
    overflow: hidden;
    background: var(--backdrop);
    font-family: "Oswald", sans-serif;
  }
  .canvas {
    position: relative;
    width: 1200px;
    height: 961px;
  }
  .label {
    position: absolute;
    left: 80px;
    top: 180px;
    width: 1040px;
    height: 600px;
    background: var(--label-white);
    overflow: hidden;
    border-radius: 6px;
  }
  .label-shapes {
    position: absolute;
    inset: 0;
    width: 100%;
    height: 100%;
  }
  .chocolate-art {
    position: absolute;
    left: 690px;
    top: 130px;
    width: 300px;
    height: 330px;
    border-radius: 46% 40% 30% 36%;
    background: radial-gradient(circle at 40% 35%, #8a5a3c 0%, #5a3422 55%, #3a1f13 100%);
  }
  .brand {
    position: absolute;
    left: 0;
    right: 0;
    top: 100px;
    display: flex;
    justify-content: center;
    align-items: center;
    gap: 12px;
  }
  .brand-mark {
    width: 34px;
    height: 34px;
    border-radius: 50%;
    background: var(--logo-blue);
  }
  .brand-name {
    font-weight: 500;
    font-size: 36px;
    color: var(--logo-blue);
    letter-spacing: 0.5px;
  }
  .product-title {
    position: absolute;
    left: 0;
    right: 0;
    top: 205px;
    text-align: center;
    color: var(--text-light);
  }
  .flavour {
    display: block;
    font-weight: 700;
    font-size: 118px;
    line-height: 1;
    letter-spacing: 2px;
    text-transform: uppercase;
  }
  .product-type {
    display: block;
    margin-top: 8px;
    font-weight: 500;
    font-size: 38px;
    letter-spacing: 2px;
    text-transform: uppercase;
  }
  .net-weight {
    position: absolute;
    left: 0;
    right: 0;
    top: 505px;
    text-align: center;
    font-weight: 500;
    font-size: 30px;
    color: var(--text-dark);
    letter-spacing: 1px;
  }
</style>
</head>
<body>
  <main class="canvas">
    <section class="label">
      <svg class="label-shapes" viewBox="0 0 1040 600" preserveAspectRatio="none" aria-hidden="true">
        <defs>
          <linearGradient id="cocoa-band" x1="0" y1="0" x2="1" y2="0">
            <stop offset="0" stop-color="var(--cocoa-mid)"/>
            <stop offset="0.5" stop-color="var(--cocoa-light)"/>
            <stop offset="1" stop-color="var(--cocoa-dark)"/>
          </linearGradient>
        </defs>
        <path d="M0,30 C260,40 560,190 1040,70 L1040,450 C720,520 360,470 0,490 Z" fill="url(#cocoa-band)"/>
        <path d="M0,60 C300,70 600,210 1040,110" fill="none" stroke="var(--label-white)" stroke-width="3" opacity="0.6"/>
      </svg>
      <div class="chocolate-art" role="img" aria-label="Chocolate bar pieces with a splash of melted chocolate"></div>
      <div class="brand">
        <span class="brand-mark"></span>
        <span class="brand-name">Radiant Harbor</span>
      </div>
      <h1 class="product-title">
        <span class="flavour">Chocolate</span>
        <span class="product-type">Protein Shake</span>
      </h1>
      <p class="net-weight">450G</p>
    </section>
  </main>
</body>
</html>
```